letter flyer TRADEUP

please see our website www.corvellpartners.com.au for details. however, we are a financial services company that has services in accounting and taxation, wealth advice, loan broking, general insurance and business advice. we want to target local potential business clients to focus on helping them conduct a review and work out what they need to do to improve the health and profitability of their business. we would like to create a letter/flyer to send them. we want the message to be as follows:
1) by having a review, we guarantee we will provide some financial benefit;
2) we are offering a cohesive and comprehensive team who will provide many financial services under one roof; and
3) we specialise in business.

we have called the campaign 'TRADEUP'

we have drafted a letter as a concept and we need design, any suggested changes in wording and imagery to demonstrate our message. We do have a logo for each of the divisions above. we thought the reverse side could just be our logo and catchphrase 'financial freedom is...'

***** we just want an A4 letter... not a bifold flyer
***** I have also included a copy of our newsletter so you can get the logos and feel for our business

```html
<!DOCTYPE html>
<html lang="en">
<head>
<meta charset="utf-8">
<title>TRADEUP Letter Flyer</title>
<link href="https://fonts.googleapis.com/css2?family=Open+Sans:wght@400;600;700&family=Roboto+Condensed:wght@400;500&family=Questrial&display=swap" rel="stylesheet">
<style>
  :root {
    --blue: #1f5fae;
    --navy: #22307a;
    --orange: #f39a1e;
    --text: #2b2b2b;
    --page: #e7e9ec;
    --paper: #ffffff;
  }
  * { margin: 0; padding: 0; box-sizing: border-box; }
  html, body { width: 1200px; height: 1200px; overflow: hidden; }
  body { background: var(--page); position: relative; font-family: "Questrial", sans-serif; color: var(--text); }

  .flyer { position: absolute; left: 212px; top: 54px; width: 775px; height: 1092px; background: var(--paper); overflow: hidden; box-shadow: 0 4px 18px rgba(0,0,0,.18); }
  .hero { position: absolute; left: 0; top: 0; width: 775px; height: 600px; }

  .brand { position: absolute; left: 31px; top: 31px; display: flex; align-items: center; gap: 14px; }
  .brand-dot { width: 78px; height: 78px; border-radius: 50%; background: var(--blue); }
  .brand-name { font-family: "Open Sans", sans-serif; font-weight: 600; font-size: 21px; line-height: 1.05; color: #4a4a4a; text-transform: uppercase; }
  .tagline { position: absolute; left: 35px; top: 132px; font-family: "Open Sans", sans-serif; font-weight: 700; font-size: 12px; color: var(--orange); }
  .campaign { position: absolute; left: 62px; top: 184px; font-family: "Roboto Condensed", sans-serif; font-weight: 500; font-size: 58px; letter-spacing: -1px; line-height: 1; }
  .campaign .lead { color: var(--blue); }
  .campaign .tail { color: #ffffff; }

  .headline-wash { position: absolute; left: 0; top: 437px; width: 300px; height: 123px; background: linear-gradient(90deg, #a7c5ec 0%, #d8e6f7 55%, rgba(255,255,255,0) 100%); }
  .headline { position: absolute; left: 50px; top: 448px; font-family: "Roboto Condensed", sans-serif; font-weight: 500; font-size: 44px; line-height: 56px; color: var(--navy); }

  .section-bar { position: absolute; left: 0; width: 344px; height: 43px; background: var(--blue); color: #fff; font-family: "Open Sans", sans-serif; font-weight: 400; font-size: 27px; line-height: 43px; padding-left: 50px; box-shadow: 3px 3px 4px rgba(0,0,0,.25); }
  .section-body { position: absolute; left: 50px; width: 380px; font-size: 16px; line-height: 22px; text-align: justify; }

  .services-bar { position: absolute; left: 472px; top: 589px; width: 303px; height: 46px; background: var(--blue); color: #fff; font-family: "Open Sans", sans-serif; font-weight: 400; font-size: 31px; line-height: 46px; padding-left: 33px; box-shadow: 3px 3px 4px rgba(0,0,0,.25); }
  .services-intro { position: absolute; left: 506px; top: 650px; width: 250px; font-size: 16px; line-height: 22px; }
  .service-list { position: absolute; left: 509px; top: 705px; list-style: none; }
  .service-list li { display: flex; align-items: center; gap: 9px; font-size: 18px; line-height: 27.5px; }
  .tick { width: 15px; height: 15px; flex: none; }
  .divider { position: absolute; left: 500px; top: 881px; width: 250px; height: 1px; background: linear-gradient(90deg, rgba(31,95,174,0), #7fa6d8 30%, #7fa6d8 70%, rgba(31,95,174,0)); }

  .address { position: absolute; left: 516px; top: 902px; display: flex; gap: 8px; }
  .address-pin { width: 18px; height: 26px; flex: none; margin-top: 2px; }
  .address-label { color: var(--blue); font-size: 14px; line-height: 17px; }
  .address-text { font-size: 14px; line-height: 18px; }

  .phone-bar { position: absolute; left: 525px; top: 984px; width: 250px; height: 47px; background: var(--orange); }
  .phone-number { position: absolute; left: 559px; top: 984px; font-family: "Roboto Condensed", sans-serif; font-size: 35px; line-height: 47px; color: #fff; }
  .phone-badge { position: absolute; left: 478px; top: 977px; width: 62px; height: 62px; }

  .footer-rule { position: absolute; left: 0; top: 1049px; width: 775px; height: 4px; background: var(--orange); }
  .footer { position: absolute; left: 0; top: 1054px; width: 775px; height: 38px; background: var(--blue); color: #fff; display: flex; align-items: center; justify-content: center; gap: 8px; font-size: 17px; }
  .globe { width: 16px; height: 16px; }
</style>
</head>
<body>
<main class="flyer">
  <svg class="hero" viewBox="0 0 775 600">
    <defs>
      <linearGradient id="warm" x1="0" y1="0" x2="0.3" y2="1">
        <stop offset="0" stop-color="#fde7c6"/>
        <stop offset="0.35" stop-color="#f9c27a"/>
        <stop offset="0.7" stop-color="#e8a35e"/>
        <stop offset="1" stop-color="#c98a4e"/>
      </linearGradient>
    </defs>
    <path role="img" aria-label="Photo of a family holding hands and walking on a beach at sunset" fill="url(#warm)" d="M0 0 H775 V548 C700 560 620 545 520 515 C360 465 180 360 0 300 Z"/>
    <path fill="#1f5fae" d="M0 252 C170 330 380 452 560 505 C620 523 680 532 745 537 C600 508 460 470 330 415 C200 362 100 326 0 302 Z"/>
    <path fill="none" stroke="#f39a1e" stroke-width="4" d="M0 306 C180 376 360 470 520 515 C620 545 700 556 775 548"/>
  </svg>

  <div class="brand">
    <div class="brand-dot"></div>
    <div class="brand-name">Corvell<br>Partners</div>
  </div>
  <div class="tagline">YOUR WEALTH ADVISORS</div>
  <div class="campaign"><span class="lead">TRADE</span><span class="tail">UP</span></div>

  <div class="headline-wash"></div>
  <h1 class="headline">We Understand<br>What Is Important To You</h1>

  <h2 class="section-bar" style="top:581px">Financial planning</h2>
  <p class="section-body" style="top:638px">If you would like to ensure you are comfortable financially now and in the future, PLANNING for this is essential.</p>

  <h2 class="section-bar" style="top:725px">Business services</h2>
  <p class="section-body" style="top:781px">As specialists to the small and medium sized business sector we offer a range of business management tools to help our clients realize the full potential of their enterprise.</p>

  <h2 class="section-bar" style="top:891px">Tax planning</h2>
  <p class="section-body" style="top:946px">In today's continually changing business and financial environment, it's vital to stay up-to-date with the many accounting industry improvements and compliance amendments.</p>

  <h2 class="services-bar">Our Services</h2>
  <p class="services-intro">We aim to provide all of your financial services, including</p>
  <ul class="service-list">
    <li><svg class="tick" viewBox="0 0 16 16"><circle cx="8" cy="8" r="6.5" fill="none" stroke="#1f5fae" stroke-width="1.4"/><path d="M5 8.2l2.2 2.2L12.5 4.5" fill="none" stroke="#1f5fae" stroke-width="1.6"/></svg>Accounting and taxation</li>
    <li><svg class="tick" viewBox="0 0 16 16"><circle cx="8" cy="8" r="6.5" fill="none" stroke="#1f5fae" stroke-width="1.4"/><path d="M5 8.2l2.2 2.2L12.5 4.5" fill="none" stroke="#1f5fae" stroke-width="1.6"/></svg>Superannuation</li>
    <li><svg class="tick" viewBox="0 0 16 16"><circle cx="8" cy="8" r="6.5" fill="none" stroke="#1f5fae" stroke-width="1.4"/><path d="M5 8.2l2.2 2.2L12.5 4.5" fill="none" stroke="#1f5fae" stroke-width="1.6"/></svg>Wealth creation</li>
    <li><svg class="tick" viewBox="0 0 16 16"><circle cx="8" cy="8" r="6.5" fill="none" stroke="#1f5fae" stroke-width="1.4"/><path d="M5 8.2l2.2 2.2L12.5 4.5" fill="none" stroke="#1f5fae" stroke-width="1.6"/></svg>Lending</li>
    <li><svg class="tick" viewBox="0 0 16 16"><circle cx="8" cy="8" r="6.5" fill="none" stroke="#1f5fae" stroke-width="1.4"/><path d="M5 8.2l2.2 2.2L12.5 4.5" fill="none" stroke="#1f5fae" stroke-width="1.6"/></svg>Insurance</li>
    <li><svg class="tick" viewBox="0 0 16 16"><circle cx="8" cy="8" r="6.5" fill="none" stroke="#1f5fae" stroke-width="1.4"/><path d="M5 8.2l2.2 2.2L12.5 4.5" fill="none" stroke="#1f5fae" stroke-width="1.6"/></svg>Business advice</li>
  </ul>
  <div class="divider"></div>

  <div class="address">
    <svg class="address-pin" viewBox="0 0 18 26"><path d="M9 1C4.6 1 1.5 4.2 1.5 8.4 1.5 14 9 22 9 22s7.5-8 7.5-13.6C16.5 4.2 13.4 1 9 1z" fill="none" stroke="#f39a1e" stroke-width="2.2"/><circle cx="9" cy="8.5" r="2.6" fill="#f39a1e"/><path d="M3 24.5h12" stroke="#f39a1e" stroke-width="2"/></svg>
    <div>
      <div class="address-label">Address:</div>
      <div class="address-text">Suite 4B 12 to 18 Harlow<br>Parade, Brindle Bay 4561</div>
    </div>
  </div>

  <div class="phone-bar"></div>
  <svg class="phone-badge" viewBox="0 0 62 62">
    <circle cx="31" cy="31" r="29" fill="#fff" stroke="#1f5fae" stroke-width="3"/>
    <circle cx="31" cy="31" r="23" fill="#f39a1e"/>
    <path d="M23 20c1.5-1.2 3-1 3.8.4l2 3.4c.7 1.2.3 2.4-.8 3.2l-1.2.9c1 2.6 3 4.8 5.5 6l1-1.2c.8-1 2.1-1.3 3.2-.6l3.4 2c1.3.8 1.5 2.3.3 3.7-1.8 2.1-4.5 2.8-7 1.6-5.6-2.6-10-7.4-12-13-.8-2.4 0-4.9 1.8-6.4z" fill="#fff"/>
  </svg>
  <div class="phone-number">1300 482 915</div>

  <div class="footer-rule"></div>
  <footer class="footer">
    <svg class="globe" viewBox="0 0 16 16"><circle cx="8" cy="8" r="6.8" fill="none" stroke="#fff" stroke-width="1.2"/><ellipse cx="8" cy="8" rx="3" ry="6.8" fill="none" stroke="#fff" stroke-width="1.1"/><path d="M1.5 8h13M2.5 4.8h11M2.5 11.2h11" stroke="#fff" stroke-width="1"/></svg>
    <span>www.corvellpartners.com.au</span>
  </footer>
</main>
</body>
</html>
```